Website for legal services (estates law) called KTV ESTATES LAW

Simple, catchy and easy to use. I am providing estates legal services and I want clients to feel a warm, friendly but professional vibe when they visit my website. I don't want harsh legal pictures (like a picture of a tough lawyer, or pictures of scales of justice). Pictures of books, plants, signing documents or a comfortable looking office are acceptable.

Please use wordpress to design it because I want ability to upload blogs on my own through wordpress after. I am attaching my logo.

Target Market(s)

Millenials, boomers, people in their 40's and anyone looking to transfer property titles or create a will, or anyone whose relatives have died and need help with estates administration.

Industry/Entity Type

Law Firm

Coding

Coded - Design and coding required

Number of Pages Required

4 page

Font styles to use
Sans Serif

Colors
0493ce
33a6d7
85cae6
cee9f5
f4fafd

Requirements
Must have
• - Must be designed with WordPress
- Must have a warm, friendly, professional vibe
- I want to be able to edit any of the content of the website myself
Nice to have
• Pictures of law books, plants, signing documents or a comfortable looking office are acceptable.
Should not have
• I don't want harsh legal pictures (like a picture of a tough lawyer, or pictures of scales of justice).

```html
<!DOCTYPE html>
<html lang="en">
<head>
<meta charset="utf-8">
<title>KTV Estates Law</title>
<link href="https://fonts.googleapis.com/css2?family=Montserrat:wght@500;600;700&family=Roboto:wght@300;400;500&display=swap" rel="stylesheet">
<style>
:root{
  --navy:#12409f;
  --navy-deep:#1a3f9b;
  --social:#1e48a6;
  --sky:#85cae6;
  --sky-btn:#7cc3e6;
  --ocean:#0493ce;
  --teal:#129a80;
  --teal-soft:#6cc3b6;
  --green:#1b9a78;
  --ink:#2a2a2a;
  --text:#3c3c3c;
  --muted:#f4f4f4;
  --white:#ffffff;
}
*{margin:0;padding:0;box-sizing:border-box}
html,body{width:1200px;height:3735px;overflow:hidden}
body{position:relative;background:var(--white);font-family:'Roboto',Arial,sans-serif;color:var(--text)}
.abs{position:absolute}
.heading{font-family:'Montserrat',Arial,sans-serif;font-weight:600;color:var(--ink)}

/* header */
.site-header{left:0;top:0;width:1200px;height:140px;background:var(--white)}
.brand{left:0;width:1200px;top:38px;text-align:center;font-family:'Montserrat',Arial,sans-serif;font-weight:600;font-size:20px;color:#333;letter-spacing:1px}
.brand-mark{display:inline-block;width:14px;height:14px;background:#333;margin-right:8px;vertical-align:-1px}
.main-nav{top:98px;left:301px;height:42px;display:flex;font-family:'Montserrat',Arial,sans-serif;font-weight:600;font-size:13px;color:#222}
.main-nav a{display:block;line-height:42px;padding:0 17px;color:inherit;text-decoration:none}
.main-nav a.active{background:var(--sky-btn);color:var(--white)}

/* hero */
.hero{left:0;top:140px;width:1200px;height:553px;background:linear-gradient(100deg,#1a1d22 0%,#2b2f36 45%,#4a4d52 70%,#2a2c30 100%)}
.hero-title{top:205px;width:1200px;text-align:center;font-family:'Montserrat',Arial,sans-serif;font-weight:600;font-size:56px;color:var(--white)}
.hero-sub{top:270px;width:1200px;text-align:center;font-family:'Montserrat',Arial,sans-serif;font-weight:400;font-size:25px;color:var(--white)}
.hero-btn{left:517px;top:335px;width:166px;height:38px;border-radius:19px;background:var(--navy);color:var(--white);font-family:'Montserrat',Arial,sans-serif;font-weight:600;font-size:13px;line-height:38px;text-align:center}
.hero-arrow{top:265px}

/* welcome */
.welcome{left:0;top:693px;width:1200px;height:300px;background:var(--navy)}
.welcome h2{position:absolute;top:52px;width:1200px;text-align:center;font-family:'Montserrat',Arial,sans-serif;font-weight:600;font-size:30px;color:var(--white)}
.welcome p{position:absolute;top:118px;left:230px;width:740px;text-align:center;font-weight:300;font-size:22px;line-height:35px;color:var(--white)}

/* about */
.about-title{left:172px;top:1072px;font-size:40px}
.about-text{left:172px;top:1134px;width:440px;font-size:13.5px;line-height:27px;color:#333}
.about-photo{left:677px;top:1088px;width:373px;height:248px;border:4px solid var(--white);box-shadow:0 2px 8px rgba(0,0,0,.25);background:linear-gradient(90deg,#4a2e1c 0%,#6b4630 30%,#2b2a30 55%,#5a3d28 100%)}

/* services */
.services{left:0;top:1439px;width:1200px;height:1328px;background:var(--muted)}
.services-title{top:1492px;width:1200px;text-align:center;font-size:40px}
.services-intro{top:1563px;width:1200px;text-align:center;font-size:14px;line-height:28px;color:#333}
.svc-photo{border:4px solid var(--white);box-shadow:0 2px 8px rgba(0,0,0,.2)}
.svc-title{font-family:'Montserrat',Arial,sans-serif;font-weight:600;font-size:29px;color:#333}
.svc-lead{font-family:'Montserrat',Arial,sans-serif;font-weight:500;font-size:16.5px;line-height:23px;color:#333}
.svc-list{list-style:none;font-size:14.5px;line-height:18px;color:#333}
.svc-list li{position:relative;padding-left:22px;margin-bottom:18px}
.svc-list svg{position:absolute;left:0;top:3px}
.pill{height:47px;border-radius:24px;color:var(--white);font-family:'Montserrat',Arial,sans-serif;font-weight:600;font-size:13.5px;line-height:47px;text-align:center}

/* social */
.social-title{top:2815px;width:1200px;text-align:center;font-size:25px}
.social-dot{width:64px;height:64px;border-radius:50%;background:var(--social);top:2878px}

/* contact */
.contact{left:0;top:2997px;width:1200px;height:492px;overflow:hidden}
.map{left:0;top:0;width:1200px;height:492px;background:linear-gradient(135deg,#eef0ec 0%,#e6ebe4 40%,#dfe9dc 70%,#eceeea 100%)}
.contact-title{left:172px;top:100px;font-family:'Montserrat',Arial,sans-serif;font-weight:700;font-size:40px;color:var(--white)}
.contact-name{left:172px;top:157px;font-family:'Montserrat',Arial,sans-serif;font-weight:600;font-size:16.5px;line-height:27px;color:var(--white)}
.contact-list{left:172px;top:238px;list-style:none;font-size:13px;color:var(--white)}
.contact-list li{position:relative;padding-left:22px;height:33px;line-height:17px}
.contact-list svg{position:absolute;left:0;top:2px}

/* footer */
.site-footer{left:0;top:3489px;width:1200px;height:246px;background:var(--navy-deep);color:var(--white)}
.footer-brand{top:82px;width:1200px;text-align:center;font-family:'Montserrat',Arial,sans-serif;font-weight:600;font-size:20px;letter-spacing:1px}
.footer-brand span{display:inline-block;width:14px;height:14px;background:var(--white);margin-right:8px;vertical-align:-1px}
.footer-nav{top:160px;width:1200px;display:flex;justify-content:center;gap:36px;font-family:'Montserrat',Arial,sans-serif;font-weight:600;font-size:13px}
.copyright{top:201px;width:1200px;text-align:center;font-size:11px}
</style>
</head>
<body>

<header class="site-header abs">
  <div class="brand abs"><span class="brand-mark"></span>KTV ESTATES LAW</div>
  <nav class="main-nav abs">
    <a class="active" href="#">HOME</a>
    <a href="#">ABOUT</a>
    <a href="#">SERVICES</a>
    <a href="#">PROJECTS</a>
    <a href="#">CONTACT</a>
    <a href="#">TAKE ACTION</a>
  </nav>
</header>

<section class="hero abs" role="img" aria-label="Photo of hands signing documents at a desk in a dim office">
  <svg class="hero-arrow abs" style="left:48px" width="22" height="40" viewBox="0 0 22 40"><path d="M20 2 L3 20 L20 38" fill="none" stroke="#fff" stroke-width="2"/></svg>
  <svg class="hero-arrow abs" style="left:1145px" width="22" height="40" viewBox="0 0 22 40"><path d="M2 2 L19 20 L2 38" fill="none" stroke="#fff" stroke-width="2"/></svg>
  <h1 class="hero-title abs">KTV ESTATES LAW</h1>
  <p class="hero-sub abs">Estates and Real Estate Law</p>
  <div class="hero-btn abs">READ MORE</div>
</section>

<section class="welcome abs">
  <h2>WELCOME TO KTV ESTATES LAW</h2>
  <p>Thank you for visiting KTV Estates Law, where I endeavor to earn your trust and provide you with high quality estates and real estate law services. My goal is to make you feel comfortable as soon as you step foot in my office.</p>
</section>

<h2 class="about-title heading abs">ABOUT</h2>
<p class="about-text abs">My name is Kira Tovell and I am an estates and real estate lawyer.<br>I graduated from Northbrook University Faculty of Law and my passion<br>is estates law and real estate law. Prior to entering the legal profession,<br>I obtained my CPA (Chartered Professional Accounting) designation<br>and worked in business and management accounting for many years,<br>where I developed a deeper understanding of money and finances. As<br>&nbsp;a lawyer, I lean on this foundation frequently for the benefit of<br>my clients.</p>
<svg class="abs" style="left:652px;top:1058px" width="425" height="310" viewBox="0 0 425 310">
  <polygon points="95,30 215,2 240,30" fill="var(--teal)"/>
  <polygon points="20,120 25,85 30,215 2,200" fill="var(--teal)"/>
  <polygon points="90,280 210,280 95,305" fill="var(--ocean)"/>
</svg>
<div class="about-photo abs" role="img" aria-label="Portrait photo of the lawyer in a suit in front of law book shelves"></div>

<section class="services abs"></section>
<h2 class="services-title heading abs">SERVICES</h2>
<p class="services-intro abs">I use my accounting background to provide a high quality legal<br>experience for my estates and real estate clients.</p>

<svg class="abs" style="left:0;top:1664px" width="540" height="452" viewBox="0 0 540 452">
  <polygon points="0,0 464,0 533,452 0,452" fill="var(--teal-soft)"/>
</svg>
<div class="svc-photo abs" style="left:141px;top:1721px;width:486px;height:334px;background:linear-gradient(120deg,#e8e4df 0%,#d8c6b4 40%,#c49a5a 60%,#e6e2dc 100%)" role="img" aria-label="Photo of a small model house on a desk with folded hands behind it"></div>
<h3 class="svc-title abs" style="left:672px;top:1716px">Estates Law</h3>
<p class="svc-lead abs" style="left:676px;top:1765px">I offer the following services as<br>part of an estate plan:</p>
<ul class="svc-list abs" style="left:674px;top:1834px;width:370px">
  <li><svg width="13" height="11" viewBox="0 0 13 11"><path d="M1 6 L5 10 L12 1" fill="none" stroke="var(--ocean)" stroke-width="2.4"/></svg>Wills (personal, corporate, foreign property);</li>
  <li><svg width="13" height="11" viewBox="0 0 13 11"><path d="M1 6 L5 10 L12 1" fill="none" stroke="var(--ocean)" stroke-width="2.4"/></svg>Trusts;</li>
  <li><svg width="13" height="11" viewBox="0 0 13 11"><path d="M1 6 L5 10 L12 1" fill="none" stroke="var(--ocean)" stroke-width="2.4"/></svg>Powers of Attorney for Personal Care and Property</li>
  <li><svg width="13" height="11" viewBox="0 0 13 11"><path d="M1 6 L5 10 L12 1" fill="none" stroke="var(--ocean)" stroke-width="2.4"/></svg>Asset planning to minimize income tax and estate administration tax upon your passing.</li>
</ul>
<div class="pill abs" style="left:674px;top:2008px;width:158px;background:var(--ocean)">READ MORE</div>

<svg class="abs" style="left:655px;top:2188px" width="545" height="452" viewBox="0 0 545 452">
  <polygon points="69,0 545,0 545,452 4,452" fill="#5fb8e2"/>
</svg>
<div class="svc-photo abs" style="left:571px;top:2247px;width:484px;height:334px;background:linear-gradient(110deg,#9aa2a6 0%,#e8e6e2 35%,#c7a07c 55%,#6d4b33 80%,#2e3f5e 100%)" role="img" aria-label="Photo of a handshake over a small model house"></div>
<h3 class="svc-title abs" style="left:172px;top:2263px">Real Estate Law</h3>
<p class="svc-lead abs" style="left:176px;top:2312px">I offer the following specialized<br>services:</p>
<ul class="svc-list abs" style="left:175px;top:2381px;width:370px">
  <li><svg width="13" height="11" viewBox="0 0 13 11"><path d="M1 6 L5 10 L12 1" fill="none" stroke="var(--green)" stroke-width="2.4"/></svg>Transfers of title to family members or spouses;</li>
  <li><svg width="13" height="11" viewBox="0 0 13 11"><path d="M1 6 L5 10 L12 1" fill="none" stroke="var(--green)" stroke-width="2.4"/></svg>Transfers of title from deceased to survivors;</li>
  <li><svg width="13" height="11" viewBox="0 0 13 11"><path d="M1 6 L5 10 L12 1" fill="none" stroke="var(--green)" stroke-width="2.4"/></svg>Transfers of title to estate trustee for the purposes of selling the estate's real estate asset.</li>
</ul>
<div class="pill abs" style="left:175px;top:2521px;width:157px;background:var(--green)">READ MORE</div>

<h2 class="social-title heading abs">CONNECT WITH SOCIAL MEDIA</h2>
<a class="social-dot abs" style="left:449px" href="#" aria-label="Social network one"></a>
<a class="social-dot abs" style="left:527px" href="#" aria-label="Social network two"></a>
<a class="social-dot abs" style="left:607px" href="#" aria-label="Social network three"></a>
<a class="social-dot abs" style="left:685px" href="#" aria-label="Social network four"></a>

<section class="contact abs">
  <div class="map abs" role="img" aria-label="Street map showing the office location"></div>
  <svg class="abs" style="left:0;top:0" width="580" height="492" viewBox="0 0 580 492">
    <polygon points="0,0 575,0 482,492 0,492" fill="var(--teal)"/>
  </svg>
  <h2 class="contact-title abs">CONTACT</h2>
  <p class="contact-name abs">KIRA M. TOVELL, BBA, CPA, CMA, JD<br>Barrister and Solicitor</p>
  <ul class="contact-list abs">
    <li><svg width="12" height="12" viewBox="0 0 12 12"><path d="M2 1 L4.5 1 L5.5 3.5 L4 4.8 Q5 7 7.2 8 L8.5 6.5 L11 7.5 L11 10 Q6 11.5 2 6.5 Q0.5 3.5 2 1Z" fill="#fff"/></svg>T: 555.280.0147</li>
    <li><svg width="12" height="12" viewBox="0 0 12 12"><rect x="3" y="1" width="6" height="4" fill="#fff"/><rect x="1" y="5" width="10" height="6" rx="1" fill="#fff"/></svg>F: 555.694.0190</li>
    <li><svg width="12" height="12" viewBox="0 0 12 12"><rect x="1" y="2.5" width="10" height="7" fill="#fff"/><path d="M1 2.5 L6 6.5 L11 2.5" fill="none" stroke="var(--teal)" stroke-width="1"/></svg>kira@ktv-law.example</li>
    <li><svg width="12" height="12" viewBox="0 0 12 12"><circle cx="6" cy="6" r="5" fill="#fff"/><path d="M1 6 H11 M6 1 Q3 6 6 11 M6 1 Q9 6 6 11" fill="none" stroke="var(--teal)" stroke-width=".8"/></svg>www.ktv-law.example</li>
    <li><svg width="12" height="13" viewBox="0 0 12 13"><path d="M6 12.5 Q1 7 1 5 A5 5 0 0 1 11 5 Q11 7 6 12.5Z" fill="#fff"/><circle cx="6" cy="5" r="1.8" fill="var(--teal)"/></svg>4200 Harbour Road, Suite 1901,<br>Lakeview ON L0L 1A1</li>
  </ul>
</section>

<footer class="site-footer abs">
  <div class="footer-brand abs"><span></span>KTV ESTATES LAW</div>
  <nav class="footer-nav abs"><span>HOME</span><span>ABOUT</span><span>SERVICES</span><span>PROJECTS</span><span>CONTACT</span></nav>
  <p class="copyright abs">Copyright 2020 All Rights Reserved</p>
</footer>

</body>
</html>
```